Larkfield Clinic Booklet 2016

Larkfield Clinic is a multi-specialty Practice in Midtown Manhattan offering advanced care in multiple areas of medicine. See our table of contents (PDF Uploaded)
Our designed booklet should be clean, easy to read, contemporary, high-end and elegant.
We need a general theme, Layout for cover and templates for internal.
We are entertaining the idea of two different sizes
8 x 10
or
11 x 8.5
Our tagline " The Future of Medicine is Here"
We will provide all the text content
The link to our website
www.LarkfieldCL.example
Uploaded files are as follows.. Logo, Our Team Photo and the PDF listing the table of contents.

```html
<!DOCTYPE html>
<html lang="en">
<head>
<meta charset="utf-8">
<title>Larkfield Clinic Booklet</title>
<link href="https://fonts.googleapis.com/css2?family=Montserrat:wght@500;600;700&family=Questrial&display=swap" rel="stylesheet">
<style>
  :root {
    --blue: #0a8fd4;
    --blue-deep: #1877c9;
    --navy: #2a3039;
    --gold: #f2b824;
    --ink: #2e3238;
    --heading-blue: #1a6eb8;
    --white: #ffffff;
    --backdrop: #dfe0e2;
    --logo-gold: #a5812f;
  }
  * { box-sizing: border-box; margin: 0; padding: 0; }
  html, body {
    width: 935px; height: 1200px; overflow: hidden;
    background: var(--backdrop);
  }
  .booklet {
    position: absolute; left: 4px; top: 0;
    width: 852px; height: 1103px;
    transform: scale(1.088); transform-origin: 0 0;
    background: var(--white);
    font-family: "Questrial", sans-serif;
    color: var(--ink);
  }
  .abs { position: absolute; }

  /* cover left */
  .brand { left: 0; top: 0; width: 495px; text-align: center; }
  .brand-mark {
    position: absolute; left: 206px; top: 42px; width: 82px; height: 82px;
    border-radius: 50%; background: var(--logo-gold);
  }
  .brand-name {
    position: absolute; left: 0; top: 143px; width: 495px;
    font-family: "Questrial", sans-serif; font-size: 22px; line-height: 24px;
    letter-spacing: 0.5px; color: var(--ink); text-transform: uppercase;
  }
  .team-photo {
    left: 0; top: 245px; width: 495px; height: 312px;
    background: linear-gradient(160deg, #c9cdd1 0%, #8aa6c6 45%, #6e8fbd 70%, #4a5566 100%);
  }
  .title-box {
    left: 0; top: 657px; width: 394px; height: 67px;
    background: linear-gradient(90deg, var(--blue-deep), var(--blue));
    color: var(--white); font-family: "Montserrat", sans-serif; font-weight: 700;
    font-size: 27px; line-height: 67px; padding-left: 40px;
  }
  .tagline-bar {
    left: 0; top: 724px; width: 495px; height: 69px; background: var(--navy);
    color: var(--white); font-size: 21px; line-height: 69px; padding-left: 40px;
    letter-spacing: 0.3px;
  }
  .divider-gold { left: 495px; top: 0; width: 4px; height: 793px; background: var(--gold); }

  /* cover right: services */
  .services { left: 499px; top: 0; width: 353px; height: 793px; background: var(--navy); }
  .band { position: absolute; left: 0; width: 353px; }
  .band-blue { background: linear-gradient(180deg, #0a8ed3, #0f86cf); }
  .band-navy { background: var(--navy); }
  .service { position: absolute; left: 0; width: 353px; color: var(--white); }
  .service-icon { position: absolute; left: 18px; width: 44px; height: 44px; }
  .service-rule { position: absolute; left: 73px; width: 2px; height: 64px; background: var(--white); }
  .service h3 {
    position: absolute; left: 97px; font-family: "Montserrat", sans-serif;
    font-weight: 600; font-size: 13.5px; white-space: nowrap;
  }
  .service ul {
    position: absolute; left: 97px; list-style: none;
    font-size: 14px; line-height: 18.5px; white-space: nowrap; opacity: 0.92;
  }

  /* inside intro */
  .intro-heading {
    left: 38px; top: 818px; font-family: "Montserrat", sans-serif;
    font-weight: 600; font-size: 24px; color: var(--ink);
  }
  .intro-heading .accent { color: var(--heading-blue); }
  .intro-copy { left: 40px; top: 872px; width: 440px; font-size: 15.2px; line-height: 20px; }
  .contact { top: 994px; font-size: 15.5px; line-height: 20px; }
  .contact-phone { left: 40px; }
  .contact-address { left: 317px; }
  .care-photo {
    left: 504px; top: 822px; width: 318px; height: 206px;
    background: linear-gradient(120deg, #eef0f2 0%, #d8dbde 40%, #b9a595 62%, #e7e8ea 100%);
  }
  .foot-blue { left: 0; top: 1065px; width: 500px; height: 38px;
    background: linear-gradient(90deg, #1a70c7, var(--blue)); }
  .foot-navy { left: 500px; top: 1065px; width: 352px; height: 38px; background: var(--navy); }
</style>
</head>
<body>
<main class="booklet">

  <header class="brand abs">
    <span class="brand-mark"></span>
    <div class="brand-name">Larkfield<br>Clinic</div>
  </header>

  <div class="team-photo abs" role="img" aria-label="Team photo of the clinic's doctors and staff in scrubs and white coats"></div>

  <h1 class="title-box abs">JOINT REJUVENATION</h1>
  <p class="tagline-bar abs">THE FUTURE OF MEDICINE IS HERE</p>
  <div class="divider-gold abs"></div>

  <section class="services abs" aria-label="Services">
    <div class="band band-navy" style="top:0;height:28px"></div>
    <div class="band band-blue" style="top:28px;height:294px"></div>
    <div class="band band-navy" style="top:322px;height:148px"></div>
    <div class="band band-blue" style="top:470px;height:295px"></div>
    <div class="band band-navy" style="top:765px;height:28px"></div>

    <div class="service" style="top:0">
      <svg class="service-icon" style="top:60px" viewBox="0 0 44 44" fill="none" stroke="#fff" stroke-width="2.6">
        <circle cx="29" cy="8" r="5"/><circle cx="12" cy="24" r="5"/><circle cx="29" cy="39" r="5"/>
        <path d="M26 12 L15 21 M15 28 L25 36"/>
      </svg>
      <span class="service-rule" style="top:68px"></span>
      <h3 style="top:41px">Functional Medicine</h3>
      <ul style="top:66px"><li>Sports Medicione</li><li>Orthopedic Medicine</li><li>Physical Therapy</li><li>Chiropractic</li><li>Custom Therapy</li></ul>
    </div>

    <div class="service" style="top:0">
      <svg class="service-icon" style="top:225px" viewBox="0 0 44 44" fill="none" stroke="#fff" stroke-width="2.8">
        <path d="M22 39 L5 20 C0 13 4 4 12 4 C17 4 20 8 22 11 C24 8 27 4 32 4 C40 4 44 13 39 20 Z"/>
      </svg>
      <span class="service-rule" style="top:216px"></span>
      <h3 style="top:189px">Alternative Medicine</h3>
      <ul style="top:229px"><li>Nutrition</li><li>Acupuncture</li></ul>
    </div>

    <div class="service" style="top:0">
      <svg class="service-icon" style="top:374px" viewBox="0 0 44 44" fill="none" stroke="#fff" stroke-width="2.8">
        <circle cx="22" cy="22" r="18"/><circle cx="25" cy="18" r="5"/>
      </svg>
      <span class="service-rule" style="top:364px"></span>
      <h3 style="top:337px">Joint Rejuvenation</h3>
      <ul style="top:368px"><li>Stem Cell Therapy</li><li>PRP</li><li>A2M</li></ul>
    </div>

    <div class="service" style="top:0">
      <svg class="service-icon" style="top:520px" viewBox="0 0 44 44" fill="none" stroke="#fff" stroke-width="2.6" stroke-linejoin="round">
        <path d="M0 23 H12 L16 13 L21 34 L25 8 L29 27 L32 23 H44"/>
      </svg>
      <span class="service-rule" style="top:511px"></span>
      <h3 style="top:485px">Diagnostics</h3>
      <ul style="top:511px"><li>Performance Testing</li><li>Advanced Ultrasound Imaging</li><li>Dynamic Xrays</li><li>Nerve Testing</li></ul>
    </div>

    <div class="service" style="top:0">
      <svg class="service-icon" style="top:667px" viewBox="0 0 44 44" fill="none" stroke="#fff" stroke-width="2.8" stroke-linejoin="round">
        <path d="M14 3 H30 M17 3 V14 C8 17 5 24 7 31 C9 38 15 41 22 41 C29 41 35 38 37 31 C39 24 36 17 27 14 V3"/>
      </svg>
      <span class="service-rule" style="top:659px"></span>
      <h3 style="top:632px">Anti-Aging Cosmetic Medicine</h3>
      <ul style="top:658px"><li>PRP for Face</li><li>PRP for Scalp</li><li>PRP for Neck</li><li>Stem Cell for Face</li><li>Botox</li></ul>
    </div>
  </section>

  <h2 class="intro-heading abs"><span class="accent">Do you want</span> know more?</h2>
  <p class="intro-copy abs">At Larkfield Clinic, we take great pride in providing the finest medical care to each and every patient. We have included information below about the different services offered in our New York office, but please call us if you have any questions!</p>
  <p class="contact contact-phone abs">Phone: 212-555-0147<br>Fax: 212-555-0192</p>
  <p class="contact contact-address abs">418 Larkfield Avenue<br>New York, NY 10099</p>

  <div class="care-photo abs" role="img" aria-label="Photo of a practitioner adjusting a seated patient's neck beside a spine model"></div>

  <div class="foot-blue abs"></div>
  <div class="foot-navy abs"></div>
</main>
</body>
</html>
```